Sole trader requires buisness card / company logo for mining and aviation

I require a business card and logo design having the following requirements;
Skyward and Engine Works
Owner: Martin Hollis
Ph: 0471593064
E: martin-r-hollis@quillmail.com.au

Logo should include a basic aircraft image and an image of an item of mining machinery either a dump truck or large excavator, but keeping in mind that the image is to be transferred onto clothing embroidery.

```html
<!DOCTYPE html>
<html lang="en">
<head>
<meta charset="utf-8">
<title>Skyward and Engine Works – Business Card</title>
<link rel="stylesheet" href="https://fonts.googleapis.com/css2?family=Overlock:wght@700&family=Special+Elite&display=swap">
<style>
  :root {
    --card-orange: #ef8e31;
    --gear-orange: #f39d3d;
    --hub-orange: #ee9034;
    --ink-green: #2f5a24;
    --logo-white: #fbeee0;
    --shadow: rgba(150, 70, 0, 0.35);
  }
  html, body {
    margin: 0;
    padding: 0;
    width: 1200px;
    height: 725px;
    overflow: hidden;
    background: var(--card-orange);
  }
  .card {
    display: block;
    width: 1200px;
    height: 725px;
    background: var(--card-orange);
  }
  .gear { filter: drop-shadow(0 6px 14px var(--shadow)); }
  .gear-teeth { fill: none; stroke: var(--gear-orange); stroke-width: 52; }
  .gear-ring { fill: var(--gear-orange); }
  .gear-hub { fill: var(--hub-orange); filter: drop-shadow(0 -3px 6px var(--shadow)); }
  .brand-name {
    font-family: "Special Elite", "Courier New", monospace;
    font-size: 34px;
    fill: var(--logo-white);
    letter-spacing: 2px;
    text-anchor: middle;
  }
  .brand-dot { fill: none; stroke: var(--logo-white); stroke-width: 3; }
  .contact {
    font-family: "Overlock", "Trebuchet MS", sans-serif;
    font-weight: 700;
    fill: var(--ink-green);
  }
  .contact-email { font-size: 33px; }
  .contact-phone { font-size: 32px; letter-spacing: 1px; }
  .contact-owner { font-size: 34px; }
</style>
</head>
<body>
<svg class="card" viewBox="0 0 1200 725" xmlns="http://www.w3.org/2000/svg">
  <defs>
    <path id="email-arc" d="M 842.5 532.5 A 205 205 0 1 1 1150 355"/>
    <path id="phone-arc" d="M 795.3 395.1 A 155 155 0 0 1 1100 355"/>
  </defs>

  <!-- Logo gear -->
  <g class="gear gear-logo">
    <circle class="gear-teeth" cx="365" cy="410" r="262" stroke-dasharray="38 30.6"/>
    <circle class="gear-ring" cx="365" cy="410" r="240"/>
    <circle class="gear-hub" cx="365" cy="410" r="205"/>
  </g>
  <g class="brand">
    <circle class="brand-dot" cx="365" cy="330" r="34"/>
    <text class="brand-name" x="365" y="420">Skyward and</text>
    <text class="brand-name" x="365" y="465">Engine Works</text>
  </g>

  <!-- Contact gear -->
  <g class="gear gear-contact">
    <circle class="gear-teeth" cx="945" cy="355" r="262" stroke-dasharray="38 30.6"/>
    <circle class="gear-ring" cx="945" cy="355" r="240"/>
    <circle class="gear-hub" cx="945" cy="355" r="205"/>
  </g>
  <g class="contact-details">
    <text class="contact contact-email" dy="-8">
      <textPath href="#email-arc" startOffset="8">E: martin-r-hollis@quillmail.com.au</textPath>
    </text>
    <text class="contact contact-phone" dy="-6">
      <textPath href="#phone-arc" startOffset="4">Ph: 0471593064</textPath>
    </text>
    <text class="contact contact-owner" x="785" y="432" transform="rotate(-21 785 432)">Owner: Martin Hollis</text>
  </g>
</svg>
</body>
</html>
```